Stage Design Company Business Card

We are looking to step up up our business card design for our team.

We are a Full service Design and Consultation company for Stage and TV with an emphasis in Theatrical Lighting.

We like our materials to be clean and modern with solid colors free of patterns and gradients. Our brand consists of 4 primary colors Purple, Black, Grey, and White. Provided is our Word Mark as well as our Symbol Logo.

We would like our cards to leave an impression beyond the information, show our attention to design and detail, and make our marks an easily recognized feature (together or apart) for our clients.

We need a warm approachable comfortable feel for some clients, and a professional flair for the board member type clients.

Attached are our brand elements, and our existing cards to give a sense of our style and a glipse at the information we provide on our cards.

Target Market(s)

broad client base from church leaders to high school teachers and architects.

Industry/Entity Type

Business

Contact Information for Business Card

We format our phone number with periods not parenthesis or dashes. Information will be edited for each of our team members, and team member specific cards are not part of this scope, but rather a template so to speak.

Font styles to use
Sans Serif

Colors
6b449b
ffffff
000000
333333
aaaaaa

Requirements
Must have
• Wordmark and logo mark present (does not need to exist on the same side of card)
• Brand Colors,
• Name, Phone, Email, Address.
• Unique choices that make someone stop and take a second look
Nice to have
• It would be nice to somehow convey what we DO, as our brand name does not lend itself to this, outside of an obvious tagline though.....
• social media if not crowded. all of our handles match (instagram, twitter, facebook)
Should not have
• "clipart"

```html
<!DOCTYPE html>
<html lang="en">
<head>
<meta charset="utf-8">
<title>Halvern Business Card</title>
<link rel="stylesheet" href="https://fonts.googleapis.com/css2?family=Jost:wght@400;500;600&display=swap">
<style>
  :root {
    --stage: #2b2b2b;
    --card: #232323;
    --card-back: #262626;
    --white: #ffffff;
    --silver: #aaaaaa;
    --purple: #4a2f86;
    --purple-line: #6b449b;
  }
  * { margin: 0; padding: 0; box-sizing: border-box; }
  html, body {
    width: 1200px; height: 900px; overflow: hidden;
    background: var(--stage);
    font-family: "Jost", sans-serif;
    color: var(--white);
  }
  .card {
    position: absolute;
    left: 250px;
    width: 700px; height: 400px;
    border-radius: 3px;
    box-shadow: 0 10px 30px rgba(0,0,0,0.45);
  }
  .card--back {
    top: 30px;
    background: var(--card-back);
    display: flex; align-items: center; justify-content: center; gap: 18px;
  }
  .brand-dot {
    width: 22px; height: 22px; border-radius: 50%;
    background: var(--silver);
  }
  .brand-name--back {
    font-size: 44px; font-weight: 500; letter-spacing: 14px;
    color: var(--silver);
  }
  .card--front {
    top: 465px;
    background: var(--card);
    overflow: hidden;
  }
  .wordmark {
    position: absolute; top: 56px; left: 0; right: 0;
    text-align: center;
    font-size: 54px; font-weight: 500;
    letter-spacing: 46px; padding-left: 46px;
    color: var(--white);
  }
  .person {
    position: absolute; top: 182px; right: 372px;
    text-align: right;
  }
  .person-name { font-size: 27px; font-weight: 600; letter-spacing: 1.5px; }
  .person-role { font-size: 19px; font-weight: 400; letter-spacing: 1px; margin-top: 2px; }
  .divider {
    position: absolute; top: 182px; left: 348px;
    width: 2px; height: 76px; background: var(--purple-line);
  }
  .contact {
    position: absolute; top: 184px; left: 372px;
    list-style: none;
    font-size: 18px; letter-spacing: 1.5px; line-height: 25px;
  }
  .contact li { display: flex; align-items: center; gap: 12px; }
  .contact svg { width: 14px; height: 14px; flex: none; }
  .address {
    position: absolute; bottom: 48px; left: 0; right: 0;
    text-align: center;
    font-size: 18px; letter-spacing: 1.5px;
  }
  .band {
    position: absolute; bottom: 0; left: 0; right: 0;
    height: 22px; background: var(--purple);
  }
</style>
</head>
<body>
  <section class="card card--back" aria-label="Card back">
    <span class="brand-dot"></span>
    <span class="brand-name--back">HALVERN</span>
  </section>

  <section class="card card--front" aria-label="Card front">
    <div class="wordmark">HALVERN</div>

    <div class="person">
      <div class="person-name">MARCUS T HALVERN</div>
      <div class="person-role">Owner</div>
    </div>

    <div class="divider"></div>

    <ul class="contact">
      <li>
        <svg viewBox="0 0 14 14" aria-hidden="true"><rect x="3.5" y="0.8" width="7" height="12.4" rx="1.2" fill="none" stroke="#fff" stroke-width="1.4"/><rect x="6" y="10.4" width="2" height="1.2" fill="#fff"/></svg>
        800.555.0142
      </li>
      <li>
        <svg viewBox="0 0 14 14" aria-hidden="true"><rect x="1" y="3" width="12" height="8.5" fill="#fff"/><path d="M1 3 L7 8 L13 3" fill="none" stroke="#232323" stroke-width="1.3"/></svg>
        info@halvern-e.com
      </li>
      <li>
        <svg viewBox="0 0 14 14" aria-hidden="true"><circle cx="5.8" cy="5.8" r="4" fill="none" stroke="#fff" stroke-width="1.8"/><line x1="8.8" y1="8.8" x2="13" y2="13" stroke="#fff" stroke-width="2"/></svg>
        halvern-e.com
      </li>
    </ul>

    <div class="address">14 N. Center ST Corvale, AZ 85390</div>
    <div class="band"></div>
  </section>
</body>
</html>
```